Salve Label

2.25 inch round label.

We are looking for a simple label, muted natural colors, sophisticated, elegant, calming.

Name of Product: Herbal Beeswax Salve
This scent is lavender - but there will be others scents
Want this label to be adaptable to other scents with simple color and word changes.

Other things to express on the label - all natural, calming, relaxing

Name of the Company: Tansy Ridge Farm
2 oz.

```html
<!DOCTYPE html>
<html lang="en">
<head>
<meta charset="utf-8">
<title>Herbal Beeswax Salve – Lavender Label</title>
<link rel="stylesheet" href="https://fonts.googleapis.com/css2?family=Dancing+Script:wght@500&family=Lobster&family=Great+Vibes&family=Lexend:wght@400&family=Montserrat:wght@700&display=swap">
<style>
  :root {
    --paper: #ffffff;
    --ink: #231f20;
    --ring-top: #7f6ad0;
    --ring-bottom: #bd7cf0;
    --ring-soft: #a99be0;
    --lavender-text: #a99be0;
    --honey-light: #fbd52a;
    --honey-deep: #f39a2b;
    --comb-tint: #fdf1bf;
    --crocus: #9a86dc;
    --stem: #8fb27c;
    --bee: #8a5a1c;
  }
  html, body {
    margin: 0;
    padding: 0;
    width: 1200px;
    height: 1200px;
    overflow: hidden;
    background: var(--paper);
  }
  .label-sheet {
    display: block;
    width: 1200px;
    height: 1200px;
  }
  .size-note {
    font-family: "Montserrat", sans-serif;
    font-weight: 700;
    font-size: 28px;
    fill: var(--ink);
  }
  .title-herbal {
    font-family: "Dancing Script", cursive;
    font-weight: 500;
    font-size: 72px;
    fill: var(--ink);
  }
  .title-beeswax {
    font-family: "Lobster", cursive;
    font-size: 140px;
  }
  .title-salve {
    font-family: "Lexend", sans-serif;
    font-size: 48px;
    fill: var(--ink);
  }
  .scent-name {
    font-family: "Great Vibes", cursive;
    font-size: 86px;
    fill: var(--lavender-text);
  }
  .farm-name {
    font-family: "Lexend", sans-serif;
    font-size: 28px;
    fill: var(--ink);
  }
  .net-weight {
    font-family: "Lexend", sans-serif;
    font-size: 27px;
    font-style: italic;
    fill: var(--ink);
  }
</style>
</head>
<body>
<svg class="label-sheet" viewBox="0 0 1200 1200" xmlns="http://www.w3.org/2000/svg">
  <defs>
    <linearGradient id="ring-gradient" x1="0" y1="0" x2="0.4" y2="1">
      <stop offset="0" stop-color="var(--ring-top)"/>
      <stop offset="1" stop-color="var(--ring-bottom)"/>
    </linearGradient>
    <linearGradient id="honey-gradient" x1="0" y1="0" x2="1" y2="0.3">
      <stop offset="0" stop-color="var(--honey-deep)"/>
      <stop offset="0.35" stop-color="var(--honey-light)"/>
      <stop offset="0.65" stop-color="var(--honey-deep)"/>
      <stop offset="1" stop-color="var(--honey-light)"/>
    </linearGradient>
    <radialGradient id="comb-gradient" cx="0.6" cy="0.5" r="0.6">
      <stop offset="0" stop-color="var(--comb-tint)" stop-opacity="0.9"/>
      <stop offset="1" stop-color="var(--comb-tint)" stop-opacity="0"/>
    </radialGradient>
    <linearGradient id="crocus-gradient" x1="0" y1="0" x2="0" y2="1">
      <stop offset="0" stop-color="var(--crocus)"/>
      <stop offset="1" stop-color="var(--stem)"/>
    </linearGradient>
    <clipPath id="label-face">
      <circle cx="604" cy="644" r="335"/>
    </clipPath>
  </defs>

  <text class="size-note" x="612" y="245" text-anchor="middle">2.25’’</text>

  <!-- label frame -->
  <g class="label-frame">
    <circle cx="604" cy="644" r="357" fill="none" stroke="url(#ring-gradient)" stroke-width="10"/>
    <circle cx="604" cy="644" r="340" fill="none" stroke="url(#ring-gradient)" stroke-width="9"/>
    <circle cx="604" cy="644" r="334" fill="none" stroke="var(--ring-soft)" stroke-width="4" opacity="0.7"/>
  </g>

  <!-- honeycomb backdrop -->
  <g clip-path="url(#label-face)">
    <path role="img" aria-label="Faint honeycomb pattern backdrop"
          d="M395 380 C470 310 620 300 760 320 C850 335 880 400 888 470 C890 520 860 550 820 545 C760 540 700 520 640 480 C560 440 470 430 395 380 Z"
          fill="url(#comb-gradient)"/>
  </g>

  <!-- product title -->
  <text class="title-herbal" x="436" y="534" textLength="167" lengthAdjust="spacingAndGlyphs">Herbal</text>
  <text class="title-beeswax" x="325" y="621" fill="url(#honey-gradient)" textLength="543" lengthAdjust="spacingAndGlyphs">Beeswax</text>
  <ellipse role="img" aria-label="Small honeybee illustration" cx="721" cy="563" rx="20" ry="22" fill="var(--bee)" opacity="0.75"/>
  <text class="title-salve" x="631" y="668" textLength="217" lengthAdjust="spacing">Salve</text>

  <!-- scent -->
  <text class="scent-name" x="602" y="758" text-anchor="middle" textLength="368" lengthAdjust="spacingAndGlyphs">Lavender scented</text>

  <!-- floral accent -->
  <ellipse role="img" aria-label="Watercolour purple crocus flowers with green stems" cx="630" cy="818" rx="72" ry="36" fill="url(#crocus-gradient)" opacity="0.55"/>

  <!-- maker and weight -->
  <text class="farm-name" x="606" y="918" text-anchor="middle">Tansy Ridge Farm</text>
  <text class="net-weight" x="609" y="954" text-anchor="middle">2oz</text>
</svg>
</body>
</html>
```